Certified Probate & Trust Postcard

Hi, I am looking for your assistance. I need a postcard design based on the following specifications. The postcard needs to be 6x9. Here are the specifications for the front and back sides. I also need help incorporating a section on the front of the postcard where I can write the name or names of the people I am addressing the postcard to, as well as a space on the back for the stamp and the receiver's address.

(revised 6/18/2025)
🖼️ FRONT SIDE

(Visual: A serene Bay Area home or warm, sunlit interior. Include Tessa’s headshot. Color palette: ivory, slate, soft gold.)

Headline:

You’ve Taken On So Much — Let Me Help with What Comes Next

Subhead:

Strategic Real Estate Guidance for Probate & Trust
Certified Probate & Trust Specialist | Serving the San Francisco Bay Area

⸻

đź“© BACK SIDE

Opening Quote (italicized):

“I lost both of my parents in 2020 — just weeks apart. That experience shaped how I serve every estate I touch.”

⸻

Main Body Copy:

My name is Tessa Varden, and I’m a Certified Probate & Trust Specialist who works with families, attorneys, and fiduciaries to guide the real estate side of probate with structure, sensitivity, and strategy.

Whether you’re navigating this with legal support or filing in pro per, this process is layered — emotional, procedural, and often overwhelming. I provide a steady hand when everything else feels uncertain.

With over a decade of experience supporting executives at Corvane, Lumirel, and Dunmore Pike, I bring the same operational precision and discretion to every estate I manage. But I also bring empathy — because I’ve been in your shoes.

⸻

What I Offer — At No Upfront Cost to the Estate:
• Property clean-outs, inspections, and basic preparation — coordinated and covered
• Real estate strategy aligned with court timelines and estate goals
• Hands-on collaboration with attorneys or step-by-step guidance for independent petitioners
• Thoughtful communication that honors your time and your grief

Because real estate isn’t just business.
For you, it’s personal. For me, it’s both.

⸻

Call to Action (in soft gold frame or slate border):

If you’re managing a probate or trust estate and need support you can trust — let’s make this easier, together.
Instagram: @itstessavoo | LinkedIn: profilehub.net/in/tessahomesagent

Industry/Entity Type

Real Estate

Requirements
Must have
• Image needs to have a calm aesthetic (remember the person receiving is grieving) emphasis on luxury as we are looking to attract high end clients so not generic and something that is easily purchased from crafto
Nice to have
• need the following design scheme as it relates to color and font Primary Color Palette: 1. Ecru Stone (Soft Beige/Taupe) – #D7CCC0 • Evokes warmth, trust, and sophistication. 2. Slate Charcoal (Deep Neutral Gray) – #4A4A4A • Represents professionalism, authority, and reliability. Accent Colors: 3. Soft Gold (Understated Elegance) – #C2B280 • Adds a subtle richness without being flashy. 4. Powder White (Clean Background Base) – #FAF9F6 • Used for breathing room, high readability, and elegance. Typography/Callout Highlight Color: 5. Trust Blue (Soft Navy) – #3F4A5F • Often used for headers or key points to add credibility and depth. Tessa Varden should be in cursive, readable and absolutely beautiful
Should not have
• No yellow, do not use ai on my image,

```html
<!DOCTYPE html>
<html lang="en">
<head>
<meta charset="utf-8">
<title>Certified Probate &amp; Trust Postcard – Tessa Varden</title>
<link href="https://fonts.googleapis.com/css2?family=Cinzel:wght@500;700&family=Great+Vibes&family=Montserrat:ital,wght@0,400;0,500;0,600;0,700;1,400;1,500&display=swap" rel="stylesheet">
<style>
  :root{
    --ecru:#D7CCC0;
    --slate:#4A4A4A;
    --gold:#C2B280;
    --gold-deep:#A8955C;
    --powder:#FAF9F6;
    --navy:#3F4A5F;
    --page:#EDEDED;
    --rule:#B9B4AC;
    --serif:'Cinzel', Georgia, serif;
    --script:'Great Vibes', cursive;
    --sans:'Montserrat', Arial, sans-serif;
  }
  *{box-sizing:border-box;margin:0;padding:0}
  html,body{width:889px;height:1200px;overflow:hidden;background:var(--page);font-family:var(--sans);color:var(--slate)}
  .canvas{position:relative;width:889px;height:1200px}
  .postcard{position:absolute;left:44px;width:800px;height:533px;background:var(--powder);box-shadow:0 2px 10px rgba(0,0,0,.12);overflow:hidden}
  .postcard--front{top:40px}
  .postcard--back{top:620px;background:#fff}

  /* brand block */
  .brand{position:absolute;display:flex;flex-direction:column;align-items:center;text-align:center}
  .brand__mark{width:26px;height:26px;border-radius:50%;background:var(--gold);margin-bottom:5px}
  .brand__name{font-family:var(--sans);font-weight:600;font-size:10px;letter-spacing:2px;color:var(--navy)}
  .brand__sub{font-family:var(--sans);font-weight:600;font-size:7px;letter-spacing:1.5px;color:var(--navy);margin-top:2px}

  /* FRONT */
  .front__left{position:absolute;left:0;top:0;width:400px;height:533px;background:#fff}
  .front__left .brand{left:0;width:400px;top:20px}
  .headline{position:absolute;left:0;width:400px;top:84px;text-align:center;color:var(--navy)}
  .headline__line{font-family:var(--serif);font-weight:700;font-size:28px;line-height:31px;letter-spacing:.5px}
  .headline__script{font-family:var(--script);font-size:31px;line-height:31px;color:var(--gold-deep)}
  .subhead{position:absolute;left:0;top:218px;width:400px;height:48px;background:var(--gold);display:flex;flex-direction:column;justify-content:center;align-items:center;font-size:10.5px;font-weight:600;color:var(--slate);line-height:15px}
  .service-area{position:absolute;left:24px;top:280px;width:352px;height:28px;background:var(--ecru);display:flex;align-items:center;gap:8px;padding-left:10px;font-size:11px;font-weight:600;color:var(--navy)}
  .service-area svg{width:14px;height:14px}
  .addressee{position:absolute;left:30px;top:332px;width:340px}
  .addressee__row{display:flex;align-items:flex-end;gap:8px;height:36px;font-size:10px;font-weight:600;color:var(--navy)}
  .addressee__row span.line{flex:1;border-bottom:1px solid var(--rule);height:1px}

  .front__photo{position:absolute;left:400px;top:0;width:400px;height:300px;background:linear-gradient(135deg,#CFC4B5 0%,#9E9488 45%,#5E5A55 100%)}
  .front__panel{position:absolute;left:400px;top:300px;width:400px;height:233px;background:var(--slate)}
  .headshot{position:absolute;left:528px;top:212px;width:150px;height:150px;border-radius:50%;border:5px solid var(--powder);background:radial-gradient(circle at 50% 40%,#A89A8A,#5A5048)}
  .agent{position:absolute;left:400px;top:378px;width:400px;text-align:center;color:var(--powder)}
  .agent__name{font-family:var(--script);font-size:56px;line-height:60px}
  .agent__title{font-family:var(--serif);font-weight:500;font-size:14px;letter-spacing:5px;margin-top:2px}
  .agent__web{position:absolute;left:400px;top:500px;width:400px;text-align:center;font-size:9px;letter-spacing:1.5px;color:var(--ecru)}

  /* BACK */
  .back__left{position:absolute;left:0;top:0;width:450px;height:533px}
  .back__brand{left:470px;width:220px;top:120px}
  .back__divider{position:absolute;left:450px;top:30px;width:1px;height:470px;background:var(--rule)}
  .quote{position:absolute;left:22px;top:24px;width:410px;height:60px;background:var(--ecru);padding:10px 30px;font-style:italic;font-weight:500;font-size:10px;line-height:14px;color:var(--navy)}
  .quote__mark{position:absolute;font-family:var(--serif);font-size:30px;font-style:normal;color:var(--gold-deep);line-height:30px}
  .quote__mark--open{left:8px;top:4px}
  .quote__mark--close{right:8px;bottom:-8px}
  .body-copy{position:absolute;left:30px;top:94px;width:395px;font-size:8px;line-height:11px;color:var(--slate)}
  .body-copy p{margin-bottom:5px}
  .offer-band{position:absolute;left:22px;top:246px;width:410px;height:22px;background:var(--navy);color:var(--powder);font-weight:700;font-size:9.5px;letter-spacing:.5px;display:flex;align-items:center;padding-left:12px}
  .offers{position:absolute;left:26px;top:276px;width:404px;display:grid;grid-template-columns:1fr 1fr;gap:6px 12px}
  .offer{display:flex;gap:7px;align-items:flex-start;font-size:8px;line-height:10.5px}
  .offer__icon{flex:none;width:20px;height:20px;border-radius:50%;background:var(--gold);display:flex;align-items:center;justify-content:center}
  .offer__icon svg{width:11px;height:11px}
  .closing{position:absolute;left:22px;top:358px;width:410px;height:64px;background:var(--ecru);text-align:center;color:var(--navy);padding-top:7px}
  .closing__lead{font-family:var(--serif);font-weight:700;font-size:14px;line-height:16px}
  .closing__script{font-family:var(--script);font-size:24px;line-height:22px;color:var(--gold-deep)}
  .closing__tail{font-size:8px;font-weight:600;margin-top:1px}
  .cta{position:absolute;left:22px;top:432px;width:410px;text-align:center;font-size:8px;line-height:11px}
  .social{position:absolute;left:22px;top:462px;width:410px;display:flex;justify-content:space-between;font-size:8px;font-weight:600;color:var(--navy)}
  .social__item{display:flex;align-items:center;gap:5px}
  .social__dot{width:12px;height:12px;border-radius:50%;background:var(--navy)}
  .stamp{position:absolute;left:705px;top:28px;width:64px;height:72px;background:#D3D3D3}
  .mailing{position:absolute;left:490px;top:250px;width:280px}
  .mailing span{display:block;height:30px;border-bottom:1px solid var(--rule)}
</style>
</head>
<body>
<div class="canvas">

  <section class="postcard postcard--front">
    <div class="front__left">
      <div class="brand">
        <div class="brand__mark"></div>
        <div class="brand__name">TESSA N. VARDEN</div>
        <div class="brand__sub">NORTHLANE REALTY</div>
      </div>
      <h1 class="headline">
        <div class="headline__line">YOU’VE TAKEN</div>
        <div class="headline__line">ON SO MUCH</div>
        <div class="headline__script">Let Me Help with</div>
        <div class="headline__line">WHAT COMES NEXT</div>
      </h1>
      <div class="subhead">
        <span>Strategic Real Estate Guidance for Probate &amp; Trust</span>
        <span>Certified Probate &amp; Trust Specialist</span>
      </div>
      <div class="service-area">
        <svg viewBox="0 0 24 24"><path d="M12 2a7 7 0 0 0-7 7c0 5 7 13 7 13s7-8 7-13a7 7 0 0 0-7-7z" fill="#3F4A5F"/><circle cx="12" cy="9" r="2.6" fill="#D7CCC0"/></svg>
        Serving the San Francisco Bay Area
      </div>
      <div class="addressee">
        <div class="addressee__row">Name: <span class="line"></span></div>
        <div class="addressee__row">Name: <span class="line"></span></div>
        <div class="addressee__row">Name: <span class="line"></span></div>
        <div class="addressee__row">Name: <span class="line"></span></div>
      </div>
    </div>
    <div class="front__photo" role="img" aria-label="Warm, sunlit living room interior of a serene Bay Area home"></div>
    <div class="front__panel"></div>
    <div class="headshot" role="img" aria-label="Headshot of Tessa Varden"></div>
    <div class="agent">
      <div class="agent__name">Tessa Varden</div>
      <div class="agent__title">REALTOR®</div>
    </div>
    <div class="agent__web">tessavarden.northlanerealty.com</div>
  </section>

  <section class="postcard postcard--back">
    <div class="back__left">
      <blockquote class="quote">
        <span class="quote__mark quote__mark--open">“</span>
        I lost both of my parents in 2020 — just weeks apart. That experience shaped how I serve every estate I touch.
        <span class="quote__mark quote__mark--close">”</span>
      </blockquote>
      <div class="body-copy">
        <p>My name is Tessa Varden, and I’m a Certified Probate &amp; Trust Specialist who works with families, attorneys, and fiduciaries to guide the real estate side of probate with structure, sensitivity, and strategy.</p>
        <p>Whether you’re navigating this with legal support or filing in pro per, this process is layered — emotional, procedural, and often overwhelming. I provide a steady hand when everything else feels uncertain.</p>
        <p>With over a decade of experience supporting executives at Corvane, Lumirel, and Dunmore Pike, I bring the same operational precision and discretion to every estate I manage. But I also bring empathy — because I’ve been in your shoes.</p>
      </div>
      <div class="offer-band">WHAT I OFFER — AT NO UPFRONT COST TO THE ESTATE:</div>
      <div class="offers">
        <div class="offer"><span class="offer__icon"><svg viewBox="0 0 24 24"><path d="M4 12l5 5L20 6" fill="none" stroke="#fff" stroke-width="3"/></svg></span><span>Property clean-outs, inspections, and basic preparation — coordinated and covered</span></div>
        <div class="offer"><span class="offer__icon"><svg viewBox="0 0 24 24"><path d="M4 12l5 5L20 6" fill="none" stroke="#fff" stroke-width="3"/></svg></span><span>Hands-on collaboration with attorneys or step-by-step guidance for independent petitioners</span></div>
        <div class="offer"><span class="offer__icon"><svg viewBox="0 0 24 24"><path d="M4 12l5 5L20 6" fill="none" stroke="#fff" stroke-width="3"/></svg></span><span>Real estate strategy aligned with court timelines and estate goals</span></div>
        <div class="offer"><span class="offer__icon"><svg viewBox="0 0 24 24"><path d="M4 12l5 5L20 6" fill="none" stroke="#fff" stroke-width="3"/></svg></span><span>Thoughtful communication that honors your time and your grief</span></div>
      </div>
      <div class="closing">
        <div class="closing__lead">Because real estate isn’t</div>
        <div class="closing__script">just business.</div>
        <div class="closing__tail">For you, it’s personal. For me, it’s both.</div>
      </div>
      <p class="cta">If you’re managing a probate or trust estate and need support you can trust — let’s make this easier, together.</p>
      <div class="social">
        <span class="social__item"><span class="social__dot"></span>@itstessavoo</span>
        <span class="social__item"><span class="social__dot"></span>profilehub.net/in/tessahomesagent</span>
      </div>
    </div>
    <div class="back__divider"></div>
    <div class="brand back__brand">
      <div class="brand__mark"></div>
      <div class="brand__name">TESSA N. VARDEN</div>
      <div class="brand__sub">NORTHLANE REALTY</div>
    </div>
    <div class="stamp"></div>
    <div class="mailing"><span></span><span></span><span></span><span></span></div>
  </section>

</div>
</body>
</html>
```